Cover for new song release

Song title: “Paper Lantern”. It’s a song about being in the moment. (Verse lyrics: “You can have your eyes wide open and still not even know...For every two steps forward take Paper Lantern and take in all the beauty all around.”

```html
<!DOCTYPE html>
<html lang="en">
<head>
<meta charset="utf-8">
<title>Paper Lantern – Single Cover</title>
<link rel="stylesheet" href="https://fonts.googleapis.com/css2?family=Montserrat:wght@800&display=swap">
<style>
  :root {
    --stage: #8a8a8a;
    --night: #04002b;
    --ember: #ff0a4c;
    --ember-soft: #c4283c;
    --crimson: #8c0f3a;
    --outline: #ffffff;
  }
  html, body {
    margin: 0;
    padding: 0;
    width: 1092px;
    height: 1200px;
    overflow: hidden;
    background: var(--stage);
  }
  .cover {
    position: absolute;
    left: 46px;
    top: 100px;
    width: 1000px;
    height: 1000px;
    display: block;
  }
  .title-type {
    font-family: "Montserrat", Arial, sans-serif;
    font-weight: 800;
  }
  .outline-edge {
    fill: none;
    stroke: #fff;
    stroke-width: 5.4;
    stroke-linejoin: miter;
  }
  .outline-hole {
    fill: #000;
    stroke: none;
  }
  .title-outline {
    fill: var(--outline);
  }
  .title-solid {
    fill: url(#title-fade);
  }
</style>
</head>
<body>
  <svg class="cover" viewBox="0 0 806 806" xmlns="http://www.w3.org/2000/svg">
    <defs>
      <radialGradient id="glow-bottom-right" cx="0.95" cy="1" r="0.6">
        <stop offset="0" stop-color="var(--ember)" stop-opacity="0.95"/>
        <stop offset="0.45" stop-color="var(--ember)" stop-opacity="0.45"/>
        <stop offset="1" stop-color="var(--ember)" stop-opacity="0"/>
      </radialGradient>
      <radialGradient id="glow-top-right" cx="0.92" cy="0" r="0.35">
        <stop offset="0" stop-color="var(--ember)" stop-opacity="0.75"/>
        <stop offset="1" stop-color="var(--ember)" stop-opacity="0"/>
      </radialGradient>
      <radialGradient id="glow-bottom-left" cx="0.05" cy="1" r="0.5">
        <stop offset="0" stop-color="var(--ember)" stop-opacity="0.7"/>
        <stop offset="1" stop-color="var(--ember)" stop-opacity="0"/>
      </radialGradient>
      <radialGradient id="glow-left" cx="0" cy="0.5" r="0.35">
        <stop offset="0" stop-color="var(--crimson)" stop-opacity="0.6"/>
        <stop offset="1" stop-color="var(--crimson)" stop-opacity="0"/>
      </radialGradient>
      <linearGradient id="title-fade" gradientUnits="userSpaceOnUse" x1="130" y1="0" x2="745" y2="0">
        <stop offset="0" stop-color="var(--ember-soft)" stop-opacity="0"/>
        <stop offset="0.28" stop-color="var(--ember-soft)" stop-opacity="1"/>
        <stop offset="0.52" stop-color="var(--ember-soft)" stop-opacity="0.8"/>
        <stop offset="1" stop-color="var(--ember-soft)" stop-opacity="1"/>
      </linearGradient>

      <!-- outer edge of the outlined word only: wide stroke minus the letter fill -->
      <mask id="paper-outline" maskUnits="userSpaceOnUse" x="0" y="0" width="806" height="806">
        <rect width="806" height="806" fill="#000"/>
        <g class="title-type" font-size="182">
          <text class="outline-edge" x="65" y="197" textLength="500" lengthAdjust="spacingAndGlyphs">PAPER</text>
          <text class="outline-hole" x="65" y="197" textLength="500" lengthAdjust="spacingAndGlyphs">PAPER</text>
        </g>
      </mask>
    </defs>

    <g class="cover-backdrop" role="img" aria-label="Dense vertical streaks of red and pink light rising over a deep navy field">
      <rect width="806" height="806" fill="var(--night)"/>
      <rect width="806" height="806" fill="url(#glow-left)"/>
      <rect width="806" height="806" fill="url(#glow-bottom-left)"/>
      <rect width="806" height="806" fill="url(#glow-top-right)"/>
      <rect width="806" height="806" fill="url(#glow-bottom-right)"/>
    </g>

    <g class="cover-title">
      <rect class="title-outline" width="806" height="806" mask="url(#paper-outline)"/>
      <text class="title-type title-solid" x="130" y="357" font-size="192" textLength="615" lengthAdjust="spacingAndGlyphs">LANTERN</text>
    </g>
  </svg>
</body>
</html>
```